HOME IMPROVEMENT Business Card

I want a very unique business card. nothing typical and boring. Im open to you ideas. Ive seen cards with gold and silver or color foil and spot UV coatings. Im looking for something that looks cool and grabs attention. I like rounded corners but am open to all suggestions. We are a home improvement company and I will have a presentation folder printed and a catalog printed also and want to keep that same theme. I love the colors in our logo but I am open at looking at a 3rd color that would work with my logo. I hope that helps.
Card should include
Address
Phone
Fax
Email
Website
Target Market(s)
Home owners, people looking to remodel their home
Industry/Entity Type
Home Improvement
Contact Information for Business Card
2873 Maple Crest Avenue Unit 410
Des Plaines, Il 60284
Phone
Direct Line
Email
Website
Font styles to use
Other font styles liked:
- IM OPEN MINDED
Requirements
Must have
- High end quality look nothing boring I like rounded corners but am open minded
Nice to have
- WOW. I want something nice and impressive.
Should not have
- ??? Not sure

```html
<!DOCTYPE html>
<html lang="en">
<head>
<meta charset="utf-8">
<title>Maplestead Business Card</title>
<link href="https://fonts.googleapis.com/css2?family=Quicksand:wght@400;500;700&family=Oswald:wght@600&display=swap" rel="stylesheet">
<style>
  :root {
    --page: #ffffff;
    --backdrop: #fee584;
    --blue: #2b7bb6;
    --blue-deep: #1f6fae;
    --silver-light: #e4e4e4;
    --silver-mid: #d2d2d2;
    --silver-dark: #9a9a9a;
    --ink-light: #f2f2f2;
    --ink-soft: #dfe6ee;
  }
  * { margin: 0; padding: 0; box-sizing: border-box; }
  html, body { width: 1200px; height: 960px; overflow: hidden; background: var(--page); }
  .backdrop {
    position: absolute; left: 2px; top: 2px; width: 1196px; height: 956px;
    background: var(--backdrop); border-radius: 56px;
  }
  .card {
    position: absolute; overflow: hidden; border-radius: 64px;
    box-shadow: 0 1px 3px rgba(0,0,0,.12);
  }
  .metal {
    background:
      repeating-linear-gradient(180deg, rgba(255,255,255,.18) 0 1px, rgba(0,0,0,0) 1px 3px, rgba(0,0,0,.04) 3px 4px),
      linear-gradient(160deg, var(--silver-light) 0%, var(--silver-light) 28%, var(--silver-dark) 40%, var(--silver-light) 52%, var(--silver-light) 72%, var(--silver-mid) 84%, var(--silver-dark) 100%);
  }
  .card-front { left: 325px; top: 137px; width: 555px; height: 325px; }
  .card-front .metal-panel { position: absolute; left: 0; top: 0; width: 221px; height: 100%; }
  .card-front .info-panel {
    position: absolute; left: 221px; top: 0; right: 0; bottom: 0;
    background:
      repeating-linear-gradient(180deg, rgba(255,255,255,.04) 0 1px, rgba(0,0,0,0) 1px 3px),
      var(--blue);
  }
  .card-back { left: 325px; top: 504px; width: 553px; height: 322px; }
  .card-back .metal-panel { position: absolute; inset: 0; }

  .brand {
    position: absolute; display: flex; align-items: center;
    font-family: "Quicksand", sans-serif; font-weight: 700; color: var(--blue-deep);
  }
  .brand .mark { background: var(--blue-deep); flex: none; }
  .brand-front { left: 12px; top: 142px; font-size: 31px; gap: 8px; }
  .brand-front .mark { width: 20px; height: 20px; }
  .brand-back { left: 120px; top: 132px; font-size: 48px; gap: 12px; }
  .brand-back .mark { width: 30px; height: 30px; }

  .person { position: absolute; left: 28px; top: 68px; color: var(--ink-light); }
  .person .name { font-family: "Quicksand", sans-serif; font-weight: 500; font-size: 29px; line-height: 1; letter-spacing: .3px; }
  .person .role { font-family: "Oswald", sans-serif; font-weight: 600; font-size: 11px; letter-spacing: 4px; margin-top: 3px; color: var(--ink-soft); }

  .contacts { position: absolute; left: 28px; top: 166px; list-style: none; color: var(--ink-light); font-family: "Quicksand", sans-serif; font-size: 11.5px; line-height: 15px; }
  .contacts li { position: relative; padding-left: 30px; margin-bottom: 6px; }
  .contacts svg { position: absolute; left: 0; width: 16px; height: 16px; fill: var(--ink-light); }
  .contacts .address svg { top: 7px; }
  .contacts .phone svg { top: 8px; }
  .contacts .email svg, .contacts .web svg { top: 0; }
  .contacts .email, .contacts .web { margin-bottom: 11px; }
</style>
</head>
<body>
  <div class="backdrop"></div>

  <section class="card card-front">
    <div class="metal-panel metal"></div>
    <div class="brand brand-front"><span class="mark"></span><span class="brand-name">Maplestead</span></div>
    <div class="info-panel">
      <div class="person">
        <p class="name">Daniel Reyes</p>
        <p class="role">GENERAL MANAGER</p>
      </div>
      <ul class="contacts">
        <li class="address">
          <svg viewBox="0 0 16 16"><path d="M8 1a5 5 0 0 0-5 5c0 3.6 5 9 5 9s5-5.4 5-9a5 5 0 0 0-5-5zm0 7a2 2 0 1 1 0-4 2 2 0 0 1 0 4z"/></svg>
          2873 Maple Crest Avenue Unit 410<br>Des Plaines, Il 60284
        </li>
        <li class="phone">
          <svg viewBox="0 0 16 16"><path d="M3.5 1.5l2.3 2.8-1.2 1.6c.9 1.9 2.4 3.4 4.3 4.4l1.6-1.2 2.8 2.3-1.3 2.1C7 13.2 2.5 8.7 1.5 3.1z"/></svg>
          99999#1<br>099999#2
        </li>
        <li class="email">
          <svg viewBox="0 0 16 16"><path d="M1 3h14v10H1zm1.5 1.2v.3L8 8.5l5.5-4V4.2zm0 2v5.6h11V6.2L8 10.2z"/></svg>
          the@email.com
        </li>
        <li class="web">
          <svg viewBox="0 0 16 16"><path d="M8 1a7 7 0 1 0 0 14A7 7 0 0 0 8 1zm0 1.3c.8.8 1.4 2.2 1.6 3.7H6.4C6.6 4.5 7.2 3.1 8 2.3zM2.4 7.2h2.8c0 .6 0 1.1.1 1.6H2.4a5.7 5.7 0 0 1 0-1.6zm4 0h3.2v1.6H6.4zm4.4 0h2.8a5.7 5.7 0 0 1 0 1.6h-2.8zM6.4 10h3.2c-.2 1.5-.8 2.9-1.6 3.7-.8-.8-1.4-2.2-1.6-3.7zM2.8 6a5.7 5.7 0 0 1 2.8-3.2C5.3 3.7 5.2 4.8 5.1 6zm8.1 0c-.1-1.2-.2-2.3-.5-3.2A5.7 5.7 0 0 1 13.2 6zM2.8 10h2.3c.1 1.2.2 2.3.5 3.2A5.7 5.7 0 0 1 2.8 10zm8.1 0h2.3a5.7 5.7 0 0 1-2.8 3.2c.3-.9.4-2 .5-3.2z"/></svg>
          thewebsite.com
        </li>
      </ul>
    </div>
  </section>

  <section class="card card-back">
    <div class="metal-panel metal"></div>
    <div class="brand brand-back"><span class="mark"></span><span class="brand-name">Maplestead</span></div>
  </section>
</body>
</html>
```